Dinner Invitation for an email

Please create an image I can embed in an email. The tone should be sophisticated, fun and festive.

Here is the copy:

FOOD | FRIENDS | FUN
Please join QBR and friends at Corvell's Harbor Room for cocktails, conversation and a delectable dinner
Date: Monday, January 23 (during NPDF)
Time: Cocktails start at 6:30 | Dinner is around 7
Place: Corvell's Harbor Room - The Pearl Terrace
27318 W Bramwick Pkwy - Scottsdale
(Adjacent to the Halloway Brightmere Lodge)

RSVP: nora.whitby@qbrvantage.com
(Nora will send you a calendar invite)

Hope to see you there!

```html
<!DOCTYPE html>
<html lang="en">
<head>
<meta charset="utf-8">
<title>QBR Dinner Invitation</title>
<link rel="stylesheet" href="https://fonts.googleapis.com/css2?family=Marcellus&family=Open+Sans:ital,wght@0,400;0,600;0,700;1,400&family=Poppins:wght@400;500&display=swap">
<style>
  :root {
    --navy: #22458a;
    --stripe-blue: #1f80d2;
    --stripe-white: #ffffff;
    --rsvp-blue: #5cb0ea;
    --text-light: #ffffff;
    --text-soft: #e6ecf7;
    --photo-dark: #2a2c30;
    --photo-mid: #6b625a;
    --photo-warm: #9a7d5e;
  }
  * { margin: 0; padding: 0; box-sizing: border-box; }
  html, body { width: 813px; height: 1200px; overflow: hidden; background: var(--navy); }
  .invitation {
    position: relative;
    width: 813px;
    height: 1200px;
    overflow: hidden;
    color: var(--text-light);
    font-family: "Open Sans", sans-serif;
    text-align: center;
  }
  .hero-photo {
    position: absolute; inset: 0 0 auto 0; height: 660px;
    background:
      radial-gradient(ellipse at 35% 65%, var(--photo-warm) 0%, transparent 45%),
      radial-gradient(ellipse at 80% 30%, #8a8c90 0%, transparent 40%),
      linear-gradient(180deg, var(--photo-dark) 0%, var(--photo-mid) 55%, #4a4540 100%);
  }
  .hero-shade {
    position: absolute; inset: 0 0 auto 0; height: 400px;
    background: linear-gradient(180deg, rgba(0,0,0,0.45), rgba(0,0,0,0.15));
  }
  .curve-bands { position: absolute; inset: 0; width: 813px; height: 1200px; }
  .block { position: absolute; left: 0; width: 100%; }

  .tagline {
    top: 192px; left: 190px; width: 433px; height: 56px;
    border-top: 1px solid rgba(255,255,255,0.75);
    border-bottom: 1px solid rgba(255,255,255,0.75);
    font-family: "Marcellus", serif; font-size: 31px; letter-spacing: 3px;
    line-height: 54px;
  }
  .tagline .divider { font-weight: 300; opacity: 0.85; padding: 0 6px; }
  .welcome { top: 290px; font-family: "Marcellus", serif; font-size: 24px; letter-spacing: 1.2px; }

  .lead-in { top: 654px; font-size: 19px; font-style: italic; color: var(--text-soft); }
  .headline { top: 686px; font-family: "Poppins", sans-serif; font-size: 26px; font-weight: 500; }
  .headline .small { font-size: 17px; font-weight: 400; }

  .date { top: 764px; font-size: 20px; font-weight: 700; }
  .date .note { font-weight: 400; }
  .time { top: 793px; font-size: 20px; font-weight: 600; }

  .venue { top: 860px; font-size: 17px; line-height: 23px; }
  .venue .adjacent { font-size: 13px; }

  .rsvp-title { top: 968px; font-family: "Marcellus", serif; font-size: 44px; color: var(--rsvp-blue); letter-spacing: 1px; }
  .rsvp-email { top: 1031px; font-size: 17px; font-weight: 600; }
  .rsvp-note { top: 1054px; font-size: 13.5px; color: var(--text-soft); }

  .brand-tile {
    position: absolute; left: 345px; top: 1113px; width: 123px; height: 87px;
    background: #ffffff; color: var(--navy);
    font-family: "Open Sans", sans-serif; font-weight: 700; font-size: 26px;
    line-height: 87px; letter-spacing: 2px;
  }
</style>
</head>
<body>
<main class="invitation">
  <div class="hero-photo" role="img" aria-label="Photo of a festive dinner table with plated appetizers and wine glasses"></div>
  <div class="hero-shade"></div>

  <svg class="curve-bands" viewBox="0 0 600 886" preserveAspectRatio="none" aria-hidden="true">
    <path d="M0 458 C 230 452 470 345 600 178 L600 886 L0 886 Z" fill="var(--stripe-white)"/>
    <path d="M0 466 C 240 460 480 350 600 196 L600 886 L0 886 Z" fill="var(--stripe-blue)"/>
    <path d="M0 476 C 250 470 490 360 600 218 L600 886 L0 886 Z" fill="var(--navy)"/>
  </svg>

  <div class="block tagline">FOOD<span class="divider">|</span>FRIENDS<span class="divider">|</span>FUN</div>
  <p class="block welcome">Please Join QBR &amp; Friends</p>

  <p class="block lead-in">for</p>
  <p class="block headline">cocktails, conversation <span class="small">and a</span> delectable dinner</p>

  <p class="block date">Monday, January 23 <span class="note">(during NPDF)</span></p>
  <p class="block time">Cocktails start at 6:30 | Dinner is around 7</p>

  <address class="block venue" style="font-style: normal;">
    Corvell's Harbor Room - The Pearl Terrace<br>
    27318 W Bramwick Pkwy - Scottsdale<br>
    <span class="adjacent">(Adjacent to the Halloway Brightmere Lodge)</span>
  </address>

  <h2 class="block rsvp-title" style="font-weight: 400;">RSVP</h2>
  <p class="block rsvp-email">nora.whitby@qbrvantage.com</p>
  <p class="block rsvp-note">(Nora will send you a calendar invite)</p>

  <div class="brand-tile">QBR</div>
</main>
</body>
</html>
```